A golden web-design opportunity

I have created a quick website (www.verimtrasystems.com.au) but I would like to have the website “polished” to look more professional and have a better consistency.

I would like the website to come across as a genuine, professional insight into our business culture but unfortunately my creative skills have reached their limit.

I have attached a media kit PDF so you are better able to establish what are about.
Updates

Hello All! I just wanted to let everyone know that I do not require an ecommerce site! My website is for potential clients to visit, see what we do and get my contact details...

Gathering more feedback

Hello All, I just wanted to let contestants know that there is not a requirement for my team to be mentioned on the website. I cover in person this as part of my presentation with clients. I have uploaded a new Presentation PDF that has this information excluded. Have a good day!

Target Market(s)

Telecommunications professionals; service delivery partners; white collar executives; construction

Industry/Entity Type

Data Communication

Coding

Coded - Design and coding required

Number of Pages Required

3 page

Font styles to use
Other font styles liked:
• Designers discretion

Colors

Designer to choose colors to be used in the design.

Requirements
Must have
• Must be designed so that I can upload it to Plesk, I think that wordpress is preferred.
• - Page:
• - 1 - Full page is a requirement i.e. the website makes full use of the whole screen
• - 2 - Colour scheme must be "muted" and not agressive
• - Links:
• - 1 - All links will work e.g. "E-Mail us" should work
• - 2 - The page identifier ("[LOGO] Home | Verimtra Sytsems) will show the Verimtra logo
• - 3 - A link to facebook and linkedin
• - https://www.facebook.com/verimtrasystems
• - https://www.linkedin.com/company/verimtra-systems-pty-ltd/
• - 4 - The phone number icon can be clicked on to make a call
• - 5 - The E-Mail icon can be clicked on to send an E-Mail
Nice to have
• Font:
• - 1 - Rounded is preferred
• - 2 - Colour with reference the logo colours (if possible)
Should not have
• Colour:
• - 1 - To much contrast between colours i.e. balck background with white writing
• - 2 - aggressive colour schemes
• - 3 - Names of Verimtra consultants... These guys are also used by my competetion, only martin is required

```html
<!DOCTYPE html>
<html lang="en">
<head>
<meta charset="utf-8">
<title>Verimtra Solutions</title>
<link href="https://fonts.googleapis.com/css2?family=Raleway:wght@400;500;600;700&family=Lato:wght@400;700&display=swap" rel="stylesheet">
<style>
:root{
  --teal:#1f86aa;
  --teal-deep:#1a7596;
  --teal-card:#3597b8;
  --slate:#1f2a31;
  --slate-deep:#182127;
  --field-dark:#2c3a42;
  --soft-light:#dde5e9;
  --paper:#fff;
  --text-dark:#2a3238;
  --text-grey:#69747a;
}
*{box-sizing:border-box;margin:0;padding:0}
html,body{width:1200px;height:3448px;overflow:hidden}
body{position:relative;background:var(--slate);color:var(--soft-light);font-family:"Lato",Arial,sans-serif}
.abs{position:absolute}
.heading{font-family:"Raleway",Arial,sans-serif;font-weight:500;text-align:center;width:100%;left:0}
.btn{position:absolute;display:flex;align-items:center;justify-content:center;background:var(--teal);color:var(--paper);border-radius:20px;font-size:13px;font-family:"Lato",Arial,sans-serif;text-decoration:none}

/* hero */
.hero{left:0;top:0;width:1200px;height:768px;overflow:hidden;color:var(--paper)}
.hero-photo{position:absolute;inset:0;background:
  radial-gradient(ellipse 340px 260px at 430px 420px,#cfcfcf 0%,#8a8a8a 45%,transparent 75%),
  radial-gradient(ellipse 260px 140px at 780px 170px,#c9c9c9 0%,#6f6a65 60%,transparent 80%),
  linear-gradient(160deg,#3a2a20 0%,#4b372a 35%,#2a2623 60%,#1e1e1f 100%)}
.hero-shade{position:absolute;inset:0;background:rgba(20,30,36,.32)}
.logo{display:flex;align-items:center;gap:10px}
.logo-dot{width:44px;height:44px;border-radius:50%;background:var(--teal)}
.logo-name{font-family:"Raleway",Arial,sans-serif;font-weight:600;font-size:30px;letter-spacing:2px;color:var(--teal);line-height:1}
.nav{top:58px;left:0;width:1200px;height:30px}
.nav a{position:absolute;top:0;color:var(--paper);font-family:"Raleway",Arial,sans-serif;font-size:14px;font-weight:600;text-decoration:none}
.nav a.active{border-bottom:3px solid var(--teal);padding-bottom:5px}
.hero-title{top:376px;font-size:36px}
.hero-sub{top:426px;font-size:15px;text-align:center;width:100%;left:0}
.arrow{width:26px;height:26px;border-radius:50%;background:var(--paper);display:flex;align-items:center;justify-content:center}
.dots{top:789px;left:578px;display:flex;gap:6px}
.dots span{width:6px;height:6px;border-radius:50%;background:#8fb9c9}
.dots span.on{background:var(--teal)}

/* story */
.section-title{font-size:27px}
.story-text{top:890px;left:280px;width:640px;text-align:center;font-size:14px;line-height:1.3}
.pillar{width:287px;height:225px;top:1064px}
.pillar-label{top:1306px;width:287px;text-align:center;font-family:"Raleway",Arial,sans-serif;font-size:25px;font-weight:500}

/* services */
.services{left:0;top:1437px;width:1200px;height:752px;background:linear-gradient(180deg,var(--teal) 0%,var(--teal-deep) 100%);color:var(--paper)}
.service{position:absolute;width:300px;text-align:center;font-family:"Raleway",Arial,sans-serif;font-size:17px;font-weight:500}
.service svg{display:block;margin:0 auto 10px}
.service-card{position:absolute;left:453px;top:122px;width:283px;height:216px;background:var(--teal-card);border-radius:10px;box-shadow:0 6px 18px rgba(0,0,0,.2)}
.card-copy{font-family:"Lato",Arial,sans-serif;font-size:11px;line-height:1.3;margin-top:6px;padding:0 46px}
.card-more{font-family:"Lato",Arial,sans-serif;font-size:12px;font-weight:700;margin-top:10px}

/* blogs */
.post{top:2313px;width:301px;height:349px;background:var(--paper);color:var(--text-dark)}
.post-photo{height:198px}
.post-meta{display:flex;justify-content:space-between;padding:10px 12px 6px;font-size:12px;font-weight:700;border-bottom:1px solid #ddd}
.post-body{padding:14px 12px}
.post-title{font-family:"Raleway",Arial,sans-serif;font-size:15px;font-weight:600}
.post-copy{font-size:11px;color:var(--text-grey);line-height:1.3;margin-top:6px}
.post-more{font-size:12px;font-weight:700;margin-top:12px}
.news-input{top:2904px;left:333px;width:513px;height:32px;border-radius:16px;background:var(--field-dark);overflow:hidden;display:flex;font-size:12px}
.news-input span{flex:1;padding:8px 20px;color:#b9c4ca}
.news-input b{width:131px;background:var(--teal);color:var(--paper);font-weight:400;display:flex;align-items:center;justify-content:center}

/* footer */
.footer{left:0;top:3028px;width:1200px;height:352px;background:var(--teal);color:var(--paper)}
.foot-head{font-family:"Raleway",Arial,sans-serif;font-weight:700;font-size:13px;border-bottom:2px solid var(--paper);padding-bottom:4px}
.foot-list{list-style:none;font-size:13px;font-weight:700;line-height:25px;margin-top:42px}
.field{position:absolute;background:var(--paper);color:#888;font-size:11px;padding:4px 10px;border-radius:8px}
.send{left:959px;top:250px;width:117px;height:26px;border-radius:13px;background:var(--slate-deep);font-size:12px;display:flex;align-items:center;justify-content:center}
.bottom{left:0;top:3380px;width:1200px;height:68px;background:var(--slate-deep)}
.social{width:26px;height:26px;border-radius:50%;background:var(--soft-light)}
</style>
</head>
<body>

<section class="abs hero">
  <div class="hero-photo" role="img" aria-label="Workspace with a white designer chair and a laptop on a wooden desk"></div>
  <div class="hero-shade"></div>
  <div class="abs logo" style="left:120px;top:48px"><span class="logo-dot"></span><span class="logo-name">VERIMTRA</span></div>
  <nav class="abs nav">
    <a class="active" style="left:727px">Home</a>
    <a style="left:789px">Our Story</a>
    <a style="left:876px">Services</a>
    <a style="left:959px">Blogs</a>
    <a style="left:1019px">Contacts</a>
  </nav>
  <h1 class="abs heading hero-title">Verimtra Solution</h1>
  <p class="abs hero-sub">Project Delivery. Done Differently.</p>
  <a class="btn" style="left:501px;top:464px;width:198px;height:37px">Read More</a>
  <div class="abs arrow" style="left:56px;top:394px"><svg width="10" height="10" viewBox="0 0 10 10"><path d="M6.5 1.5 3 5l3.5 3.5" fill="none" stroke="#1f2a31" stroke-width="1.8"/></svg></div>
  <div class="abs arrow" style="left:1132px;top:394px"><svg width="10" height="10" viewBox="0 0 10 10"><path d="M3.5 1.5 7 5 3.5 8.5" fill="none" stroke="#1f2a31" stroke-width="1.8"/></svg></div>
</section>

<div class="abs dots"><span class="on"></span><span></span><span></span><span></span></div>

<h2 class="abs heading section-title" style="top:838px">Our Story</h2>
<p class="abs story-text">We are an innovative telecommunications services company. We believe technology can truly change peoples' lives, so we are working with Victoria's most respected delivery partners to complete unique projects state-wide.</p>
<a class="btn" style="left:501px;top:966px;width:198px;height:39px">Read More</a>

<div class="abs pillar" style="left:122px;background:radial-gradient(circle at 60% 45%,#9fd4f5 0%,#2c6fc0 35%,#0b2a66 80%)" role="img" aria-label="Glowing global network over the earth"></div>
<div class="abs pillar" style="left:455px;background:linear-gradient(135deg,#c9d0d4 0%,#7b9a6e 40%,#c9563f 70%,#9fb0b8 100%)" role="img" aria-label="Hands joining coloured puzzle pieces"></div>
<div class="abs pillar" style="left:791px;background:radial-gradient(circle at 45% 60%,#e8e4dc 0%,#b7b0a4 55%,#6d665c 100%)" role="img" aria-label="Compass dial pointing to integrity"></div>
<div class="abs pillar-label" style="left:122px;top:1302px">Innovation</div>
<div class="abs pillar-label" style="left:455px">Collaboration</div>
<div class="abs pillar-label" style="left:791px">Integrity</div>

<section class="abs services">
  <h2 class="abs heading section-title" style="top:58px">Our Services</h2>
  <div class="service-card"></div>

  <div class="service" style="left:91px;top:148px">
    <svg width="60" height="62" viewBox="0 0 60 62" fill="none" stroke="#fff" stroke-width="2.4"><rect x="12" y="8" width="36" height="48" rx="3"/><rect x="22" y="3" width="16" height="9" rx="2"/><path d="M20 24h20M20 32h20M20 40h12"/><circle cx="13" cy="46" r="7"/></svg>
    Project<br>Management
  </div>
  <div class="service" style="left:445px;top:148px">
    <svg width="60" height="62" viewBox="0 0 60 62" fill="none" stroke="#fff" stroke-width="2.4"><path d="M8 8h44v46H8zM19 8v46M30 8v46M41 8v46M8 14l11-4M19 14l11-4M30 14l11-4M41 14l11-4"/></svg>
    Asbestos Removal
    <p class="card-copy">Lorem Ipsum is simply dummy the printing and typesetting.</p>
    <p class="card-more">Continue.. &#8594;</p>
  </div>
  <div class="service" style="left:818px;top:148px">
    <svg width="60" height="62" viewBox="0 0 60 62" fill="none" stroke="#fff" stroke-width="2.4"><rect x="4" y="26" width="10" height="20"/><rect x="46" y="26" width="10" height="20"/><path d="M14 30h32M14 42h32"/><rect x="24" y="14" width="12" height="16"/><path d="M20 14h20"/></svg>
    Pit and Pipe<br>installation
  </div>

  <div class="service" style="left:91px;top:370px">
    <svg width="60" height="62" viewBox="0 0 60 62" fill="none" stroke="#fff" stroke-width="2.4"><rect x="14" y="6" width="28" height="8"/><rect x="14" y="48" width="28" height="8"/><path d="M18 14v34M24 14v34M30 14v34M36 14v34M42 40c8 0 12 6 8 14"/></svg>
    Cable Hauling
  </div>
  <div class="service" style="left:445px;top:370px">
    <svg width="60" height="62" viewBox="0 0 60 62" fill="none" stroke="#fff" stroke-width="2.4"><path d="M14 54l16-22M30 32l10-18M30 32l16-6M30 32l16 6M30 32l6 12"/><circle cx="42" cy="12" r="3"/><circle cx="49" cy="25" r="3"/><circle cx="49" cy="39" r="3"/><circle cx="38" cy="46" r="3"/></svg>
    Fibre splicing
  </div>
  <div class="service" style="left:818px;top:370px">
    <svg width="60" height="62" viewBox="0 0 60 62" fill="none" stroke="#fff" stroke-width="2.4"><path d="M10 52h14V30a8 8 0 0 1 16 0v-12"/><rect x="34" y="8" width="12" height="10"/><rect x="6" y="46" width="8" height="12"/></svg>
    Copper Jointing
  </div>

  <div class="service" style="left:91px;top:540px">
    <svg width="60" height="62" viewBox="0 0 60 62" fill="none" stroke="#fff" stroke-width="2.4"><circle cx="30" cy="8" r="4"/><circle cx="14" cy="14" r="4"/><circle cx="46" cy="14" r="4"/><path d="M30 12v42M14 18v12l10 8v16M46 18v12l-10 8v16M22 26v10M38 26v10"/></svg>
    Fibre integration
  </div>
  <div class="service" style="left:445px;top:540px">
    <svg width="60" height="62" viewBox="0 0 60 62" fill="none" stroke="#fff" stroke-width="2.6"><path d="M14 18A22 22 0 1 1 10 38"/><path d="M14 8v10h10"/><path d="M32 20v14h10"/></svg>
    Recoverable works
  </div>
  <div class="service" style="left:818px;top:540px">
    <svg width="60" height="62" viewBox="0 0 60 62" fill="none" stroke="#fff" stroke-width="2.4"><circle cx="30" cy="14" r="4"/><path d="M20 6a14 14 0 0 0 0 16M40 6a14 14 0 0 1 0 16M14 2a20 20 0 0 0 0 24M46 2a20 20 0 0 1 0 24M30 18L18 58M30 18l12 40M22 44h16M26 32h8M18 58l18-14M42 58L24 44"/></svg>
    Telecommunication Rigging
  </div>
</section>

<h2 class="abs heading section-title" style="top:2244px">Blogs</h2>

<article class="abs post" style="left:122px">
  <div class="post-photo" style="background:linear-gradient(160deg,#8a8f93 0%,#4f6f99 45%,#3a4656 100%)" role="img" aria-label="Worker in protective mask and overalls at an industrial site"></div>
  <div class="post-meta"><span>&#9636; July 01 , 2018</span><span>&#9825; 20 &nbsp;&#9633; 12</span></div>
  <div class="post-body"><p class="post-title">Blog Post Title 01</p><p class="post-copy">Lorem Ipsum is simply dummy the printing and typesetting.</p><p class="post-more">Continue.. &#8594;</p></div>
</article>
<article class="abs post" style="left:448px">
  <div class="post-photo" style="position:relative;background:linear-gradient(150deg,#7a6651 0%,#b9a88e 45%,#5b4a39 100%)" role="img" aria-label="Cable being laid in an open trench">
    <svg class="abs" style="left:132px;top:80px" width="38" height="38" viewBox="0 0 38 38"><circle cx="19" cy="19" r="17" fill="none" stroke="#fff" stroke-width="2"/><path d="M15 12l11 7-11 7z" fill="#fff"/></svg>
  </div>
  <div class="post-meta"><span>&#9636; June 01 , 2018</span><span>&#9825; 20 &nbsp;&#9633; 12</span></div>
  <div class="post-body"><p class="post-title">Blog Post Title 01</p><p class="post-copy">Lorem Ipsum is simply dummy the printing and typesetting.</p><p class="post-more">Continue.. &#8594;</p></div>
</article>
<article class="abs post" style="left:777px">
  <div class="post-photo" style="background:linear-gradient(140deg,#3b4a3c 0%,#5f8f4e 40%,#c76a35 65%,#2b2f33 100%)" role="img" aria-label="Technician splicing coloured fibre optic cables"></div>
  <div class="post-meta"><span>&#9636; June 01 , 2018</span><span>&#9825; 20 &nbsp;&#9633; 12</span></div>
  <div class="post-body"><p class="post-title">Blog Post Title 01</p><p class="post-copy">Lorem Ipsum is simply dummy the printing and typesetting.</p><p class="post-more">Continue.. &#8594;</p></div>
</article>

<a class="btn" style="left:508px;top:2720px;width:198px;height:37px">View More</a>

<h2 class="abs heading" style="top:2828px;font-size:23px">Join The Newsletter</h2>
<p class="abs" style="top:2864px;width:100%;text-align:center;font-size:13px">Sign up for Our Newsletter</p>
<div class="abs news-input"><span>Email here</span><b>Subscribe</b></div>

<footer class="abs footer">
  <div class="abs logo" style="left:122px;top:90px"><span class="logo-dot" style="background:var(--paper)"></span><span class="logo-name" style="color:var(--paper)">VERIMTRA</span></div>
  <p class="abs" style="left:122px;top:172px;width:272px;font-size:12.5px;font-weight:700;line-height:1.35">Lorem Ipsum is a simply dummy text of the printing and typesetting indu story Lorem text of the printing and typeset Ipsum.industries.</p>
  <p class="abs" style="left:122px;top:250px;font-size:13px;font-weight:700">Read More.. &#8594;</p>

  <div class="abs" style="left:430px;top:86px"><p class="foot-head">QUICK LINKS</p>
    <ul class="foot-list" style="line-height:26px"><li>&#8594; Home</li><li>&#8594; Our Story</li><li>&#8594; Services</li><li>&#8594; Blogs</li><li>&#8594; Contacts</li></ul></div>

  <div class="abs" style="left:616px;top:86px"><p class="foot-head">CONTACT US</p>
    <ul class="foot-list"><li>48 Harbourline Road,</li><li>Brookvale 2100</li><li>Australia.</li><li>+61 455 018 372</li><li>info@verimtrasystems.com.au</li></ul></div>

  <div class="abs" style="left:851px;top:86px;width:225px"><p class="foot-head">QUICK CONTACT</p></div>
  <div class="field" style="left:851px;top:154px;width:110px;height:21px">Name</div>
  <div class="field" style="left:966px;top:154px;width:110px;height:21px">Phone</div>
  <div class="field" style="left:851px;top:181px;width:225px;height:51px">Message</div>
  <div class="abs send">Send</div>
</footer>

<div class="abs bottom">
  <p class="abs" style="left:122px;top:25px;font-size:14px;font-weight:700">Copyright &copy; 2018 Verimtra Solutions.&nbsp; All Rights Reserved.</p>
  <div class="abs" style="left:906px;top:21px;display:flex;gap:11px"><span class="social"></span><span class="social"></span><span class="social"></span><span class="social"></span><span class="social"></span></div>
</div>

</body>
</html>
```